Business Card Design Project

We require a professional business card designed for our consulting organisation that has the same theme and colours as our logo except for the grey.

Colours on the front should predominately be white however some reference to our logo colours except for the grey.

The back of the card should be have background colour that aligns with our logo colour.

Layout, style and design is up to the designer. So send through your designs

Details are attached in the word document project brief.

Target Market(s)

Target market are large corporate organisations

Industry/Entity Type

Business

Requirements
Must have
• Content on the front must have:

Dean Halvorsen
Managing Director

P: 0417 285 394
E: Dean@brevolinkpartners.com
W: www.brevolinkpartners.com

Content on the back must have the words:
Alliances
Placement
Training
Support

Design Colours
Must align to our logo

```html
<!DOCTYPE html>
<html lang="en">
<head>
<meta charset="utf-8">
<title>Brevolink Partners – Business Card</title>
<link rel="stylesheet" href="https://fonts.googleapis.com/css2?family=Montserrat:wght@400;500;600;700&display=swap">
<style>
  :root {
    --bg: #2a2a2c;
    --blue-light: #1ea0e0;
    --blue-mid: #0a8fd4;
    --blue-deep: #0677b8;
    --blue-stripe: #0b5fae;
    --white: #ffffff;
    --paper: #f3f4f5;
    --brand-blue: #0a77c4;
  }
  * { margin: 0; padding: 0; box-sizing: border-box; }
  html, body {
    width: 1200px;
    height: 900px;
    overflow: hidden;
    background: var(--bg);
    font-family: "Montserrat", sans-serif;
  }
  .sheet {
    width: 1200px;
    height: 900px;
    display: flex;
    flex-direction: column;
    align-items: center;
    justify-content: center;
    gap: 40px;
  }
  .card {
    position: relative;
    width: 700px;
    height: 400px;
    overflow: hidden;
    box-shadow: 0 10px 28px rgba(0, 0, 0, 0.55);
  }
  .card-art {
    position: absolute;
    inset: 0;
    width: 100%;
    height: 100%;
  }

  /* Front */
  .brand {
    position: absolute;
    left: 48px;
    top: 92px;
    display: flex;
    align-items: center;
    gap: 16px;
  }
  .brand-mark {
    width: 44px;
    height: 44px;
    border-radius: 50%;
    background: var(--brand-blue);
  }
  .brand-name {
    font-weight: 700;
    font-size: 40px;
    line-height: 1;
    letter-spacing: 0.5px;
    color: var(--brand-blue);
  }
  .contact {
    position: absolute;
    left: 300px;
    top: 232px;
    color: var(--white);
  }
  .contact-name {
    font-weight: 500;
    font-size: 23px;
    letter-spacing: 1.5px;
    text-transform: uppercase;
  }
  .contact-role {
    font-weight: 500;
    font-size: 15px;
    letter-spacing: 0.5px;
    margin-top: 2px;
  }
  .contact-lines {
    list-style: none;
    margin-top: 26px;
    font-size: 16px;
    font-weight: 500;
    line-height: 1.45;
    letter-spacing: 0.5px;
  }

  /* Back */
  .card-back {
    background: linear-gradient(135deg, var(--blue-light) 0%, var(--blue-mid) 55%, var(--blue-deep) 100%);
  }
  .services {
    position: absolute;
    right: 26px;
    top: 50%;
    writing-mode: vertical-rl;
    transform: translateY(-50%) rotate(180deg);
    white-space: nowrap;
    color: var(--white);
    font-size: 12px;
    font-weight: 500;
    line-height: 1;
    letter-spacing: 1.5px;
    text-transform: uppercase;
  }
</style>
</head>
<body>
<main class="sheet">

  <section class="card card-front">
    <svg class="card-art" viewBox="0 0 700 400" preserveAspectRatio="none" aria-hidden="true">
      <defs>
        <linearGradient id="frontBlue" x1="0" y1="0" x2="1" y2="1">
          <stop offset="0" stop-color="#1ea6e4"/>
          <stop offset="0.6" stop-color="#0b8fd3"/>
          <stop offset="1" stop-color="#0676b6"/>
        </linearGradient>
        <linearGradient id="frontWhite" x1="0" y1="0" x2="0" y2="1">
          <stop offset="0" stop-color="#ffffff"/>
          <stop offset="1" stop-color="#e9ebed"/>
        </linearGradient>
      </defs>
      <rect width="700" height="400" fill="url(#frontBlue)"/>
      <path d="M0 0 H700 V40 C560 150 300 205 0 212 Z" fill="url(#frontWhite)"/>
      <path d="M0 212 C300 205 560 150 700 40 V52 C560 164 300 218 0 224 Z" fill="var(--blue-stripe)"/>
      <path d="M0 224 C300 218 560 164 700 52 V58 C560 172 300 226 0 232 Z" fill="#ffffff" opacity="0.85"/>
      <path d="M130 400 C120 320 150 260 210 230 L240 228 C190 260 165 320 175 400 Z" fill="#ffffff" opacity="0.05"/>
    </svg>

    <div class="brand">
      <span class="brand-mark"></span>
      <span class="brand-name">Brevolink Partners</span>
    </div>

    <div class="contact">
      <h1 class="contact-name">Dean Halvorsen</h1>
      <p class="contact-role">Managing Director</p>
      <ul class="contact-lines">
        <li>P:&nbsp; 0417 285 394</li>
        <li>E:&nbsp; Dean@brevolinkpartners.com</li>
        <li>W: www.brevolinkpartners.com</li>
      </ul>
    </div>
  </section>

  <section class="card card-back">
    <p class="services">Alliances • Placement • Training • Support</p>
  </section>

</main>
</body>
</html>
```